Craft oriented film company needs a Business Card design

Hi all,
We're a 2-man band film company in New Zealand called Kestrel Pictures. We're good honest blokes, who are very passionate about the craft of film making. I've attached our current logo which has a bit of a crafty/artisan feel that we like. Feel free to use it - or throw the baby out with the bathwater and start again..... you never know, you might inspire a complete brand re-work.

In any case, the vibe we want to give out is that we are solid, dependable and no bullshit - but without compromising creative excellence and being in the now. We like the 'Brooklyn' artisan style of work.

Preferably single sided.

We need the standard stuff:
Name, job title, cellphone, email address and physical address (this can be smaller if you like - street, suburb, city & zip, country [if you want])

Check out our website to learn more about us: kestrelpictures.example

Target Market(s)

Brand marketers and advertising agency creatives looking for video production.

Industry/Entity Type

Baby

Requirements
Should not have
• Nothing flashy or too 'futuristic', we want it to feel grounded and real. A limited colour palette is preferred.
We don't want any film reels or cameras or anything obvious like that.

```html
<!DOCTYPE html>
<html lang="en">
<head>
<meta charset="utf-8">
<title>Kestrel Pictures — Business Card</title>
<link href="https://fonts.googleapis.com/css2?family=Merriweather:wght@400;700&display=swap" rel="stylesheet">
<style>
  :root {
    --backdrop: #d9d9d9;
    --card: #f4f4f2;
    --ink: #1e1e1e;
    --ink-soft: #3a3a3a;
  }
  * { margin: 0; padding: 0; box-sizing: border-box; }
  html, body {
    width: 1200px;
    height: 750px;
    overflow: hidden;
    background: var(--backdrop);
    font-family: "Merriweather", Georgia, serif;
    color: var(--ink);
  }
  .stage {
    width: 1200px;
    height: 750px;
    display: flex;
    align-items: center;
    justify-content: center;
  }
  .business-card {
    width: 340px;
    height: 620px;
    background: var(--card);
    border-radius: 24px;
    padding: 44px 40px 46px;
    display: flex;
    flex-direction: column;
  }
  .brand {
    display: flex;
    align-items: center;
    justify-content: flex-end;
    gap: 10px;
  }
  .brand-dot {
    width: 30px;
    height: 30px;
    border-radius: 50%;
    background: var(--ink);
    flex: none;
  }
  .brand-name {
    font-size: 13px;
    font-weight: 700;
    letter-spacing: 0.08em;
    text-transform: uppercase;
  }
  .person { margin-top: 56px; }
  .person-name {
    font-size: 25px;
    font-weight: 700;
    text-transform: uppercase;
    letter-spacing: 0.01em;
    line-height: 1.1;
  }
  .person-role {
    margin-top: 6px;
    font-size: 14px;
    letter-spacing: 0.42em;
    text-transform: uppercase;
    color: var(--ink-soft);
  }
  .phone {
    margin-top: 34px;
    font-size: 27px;
    font-weight: 400;
    letter-spacing: 0.01em;
  }
  .divider-cross {
    display: block;
    margin: 22px 0 22px 50px;
  }
  .contact-details {
    font-size: 10.5px;
    line-height: 1.75;
    text-transform: uppercase;
    letter-spacing: 0.02em;
    color: var(--ink-soft);
  }
  .rule {
    margin-top: auto;
    height: 5px;
    background: var(--ink);
  }
  .website {
    margin-top: 22px;
    font-size: 15px;
    font-weight: 700;
    text-transform: uppercase;
    letter-spacing: 0.01em;
  }
</style>
</head>
<body>
  <main class="stage">
    <article class="business-card">
      <header class="brand">
        <span class="brand-dot"></span>
        <span class="brand-name">Kestrel Pictures</span>
      </header>

      <section class="person">
        <h1 class="person-name">Rowan Tate</h1>
        <p class="person-role">Producer</p>
      </section>

      <p class="phone">+64-21-555-0142</p>

      <svg class="divider-cross" width="30" height="30" viewBox="0 0 30 30" aria-hidden="true">
        <line x1="3" y1="3" x2="27" y2="27" stroke="#1e1e1e" stroke-width="1.4"/>
        <line x1="27" y1="3" x2="3" y2="27" stroke="#1e1e1e" stroke-width="1.4"/>
      </svg>

      <address class="contact-details">
        rowan@kestrelpictures.example<br>
        12 Harbour Lane, Westmere<br>
        Auckland 1022
      </address>

      <div class="rule"></div>
      <p class="website">kestrelpictures.example</p>
    </article>
  </main>
</body>
</html>
```